Design "RIDGEMANTIS" Hearthcart online store for hunting, outdoor and tactical accessories, appare

Design and setup Hearthcart platform online store for hunting, outdoor and tactical accessories, apparel.

Logo has been uploaded. Instagram, Facebook and domain all setuop

A really modern easy to navigate online store that I can add and remove categories, add and remove products, update images, slider images, must have a AUD, USD, EUR, NZD and GBP currency converter drop down. RRPs will start in AUD. domain name is already registered and logo is done. Products are being photographed in readiness for you to set up the site. Fast shopping cart as guest with just name and address vs joining and collecting info for newsletters. Ability to send out newsletters. Home page that showcases 4-6 key categories of the site with hero images that can be updated by me. A clear navigation pane across the top. In the shopping part a clear categories navigation that can be updated as required. Free postage Australia and NZ, international shipment extra. Ultimately I need a great design as we have great products appealing to hunters, people who love the outdoors from camping to hiking, to tactical supplies. It's important to be strong website that shows quality and is easy to get arouund. Most of all it is brand new so whatever you can do to help drive traffic to it please do so. I will be managing it when ready with view to hiring a social media/web analyst to support me in a month.

Target Market(s)

Australian hunters and outdoor lovers - camping, hiking, motorbikes (dirt bikes / MX), and tactical professionals

Industry/Entity Type

Online Shopping

Coding

Coded - Design and coding required

Number of Pages Required

5+ page

Requirements
Must have
• As per my description plus up to the designers. You are the experts. I want it to look great but ultimately it has to get traffic and SELL PRODUCT
• Would like option for people to review products, eg leave 1-5 stars.
• After pay and Paypal for payment is my suggestion but I'm not the expert
• Work on computers, tablets and smartphones - compatible for all devices
Nice to have
• Product thumbnails, rankings. Can click on product to see more pictures, video and details. Size charts for apparel.
• Products will be things such as bags, equipment, accessories, clothing - all designed for outdoor activities predominantly hunting, camping, MX dirt bike riding, fishing, etc

```html
<!DOCTYPE html>
<html lang="en">
<head>
<meta charset="utf-8">
<title>RIDGEMANTIS — Hunting, Outdoor &amp; Tactical Store</title>
<link rel="stylesheet" href="https://fonts.googleapis.com/css2?family=Open+Sans:wght@400;600;700;800&family=Oswald:wght@500;600&display=swap">
<style>
:root{
  --orange:#f7941d;
  --orange-dark:#e07f0b;
  --black:#0b0b0b;
  --nav:#4a4a4a;
  --text:#222;
  --muted:#8a8a8a;
  --line:#e3e3e3;
  --footer:#121212;
  --footer-text:#9a9a9a;
  --blue:#1a73e8;
}
*{box-sizing:border-box;margin:0;padding:0}
html,body{width:1200px;height:3175px;overflow:hidden;background:#fff}
body{position:relative;font-family:"Open Sans",Arial,sans-serif;color:var(--text)}
.abs{position:absolute}

/* top bar */
.topbar{left:0;top:0;width:1200px;height:34px;background:#fff;font-size:10px;color:#333}
.topbar .contact{left:88px;top:10px;display:flex;gap:24px;align-items:center}
.topbar .util{right:88px;top:10px;display:flex;gap:40px}
.ico-sq{display:inline-block;width:10px;height:7px;background:#333;margin-right:6px;vertical-align:middle}
.flag{display:inline-block;width:12px;height:8px;background:#1f3a8a;margin:0 4px;vertical-align:middle}

/* header */
.header{left:0;top:34px;width:1200px;height:97px;background:var(--black)}
.logo{left:85px;top:20px;display:flex;align-items:center;gap:10px}
.logo-mark{width:14px;height:14px;background:var(--orange)}
.logo-name{font-weight:800;font-size:30px;color:var(--orange);letter-spacing:1px}
.search{left:603px;top:32px;width:313px;height:34px;background:#fff;border-radius:17px;display:flex;align-items:center;font-size:10px;color:#555;padding:0 14px}
.search .cat{padding-right:14px;border-right:1px solid #ccc}
.search .field{flex:1;padding-left:12px;color:#aaa}
.cart{left:952px;top:42px;font-size:13px;font-style:italic;color:#fff;font-weight:600}
.cart em{color:var(--orange)}
.cart-icon{left:1066px;top:33px}

/* nav */
.nav{left:0;top:131px;width:1200px;height:43px;background:var(--nav)}
.nav a{position:absolute;top:0;height:43px;line-height:43px;color:#fff;font-size:13px;font-weight:600;text-decoration:none;white-space:nowrap}
.nav a.active{background:var(--orange);padding:0 10px}
.caret{font-size:9px;margin-left:4px}

/* hero */
.hero{left:0;top:174px;width:1200px;height:433px;background:linear-gradient(180deg,#0e0e12 0%,#221a1a 40%,#7a2a10 62%,#2a1510 80%,#0a0a0a 100%)}
.hero-title{left:322px;top:328px;width:537px;height:95px;border:4px solid #fff;color:#fff;font-size:38px;font-weight:600;letter-spacing:3px;display:flex;align-items:center;justify-content:center}
.btn{background:var(--orange);color:#fff;font-weight:700;text-transform:uppercase;border-radius:16px;display:flex;align-items:center;justify-content:center}
.hero-btn{left:529px;top:453px;width:131px;height:36px;border-radius:0;font-size:13px}
.arrow{color:#fff;font-size:46px;font-weight:300;line-height:1}
.dots{left:565px;top:570px;display:flex;gap:7px}
.dots i{width:8px;height:8px;border-radius:50%;background:#fff}
.dots i.on{background:var(--orange)}

/* dropdown */
.dropdown{left:159px;top:174px;width:300px;height:143px;background:#1c1c1c;padding:10px 8px;display:flex;gap:42px}
.dropdown h4{color:#fff;font-size:11px;font-weight:700;margin-bottom:6px}
.dropdown li{list-style:none;color:#ddd;font-size:10px;border-top:1px solid #444;width:115px;height:28px;line-height:28px;padding-left:10px}
.dropdown li::before{content:"›";margin-right:8px}

/* category tiles */
.tile{width:313px;height:214px;color:#fff;text-align:center}
.tile .frame{position:absolute;inset:17px 17px 17px 17px;border:3px solid #fff;display:flex;flex-direction:column;align-items:center;justify-content:center;text-transform:uppercase;text-shadow:0 1px 3px rgba(0,0,0,.5)}
.tile .l1{font-size:31px;font-weight:700;line-height:1.05}
.tile .l2{font-size:27px;font-weight:600;line-height:1.1}

/* section headings */
.section-title{left:0;width:1200px;text-align:center;font-size:29px;font-weight:700;color:#111}
.underline{left:567px;width:66px;height:4px;background:var(--orange)}

/* products */
.product{width:203px}
.product .img{height:212px;border:1px solid var(--line)}
.product .name{margin-top:20px;font-size:11px;font-weight:700;text-transform:uppercase;white-space:nowrap}
.product .price{margin-top:6px;font-size:12px;padding-left:40px}
.product .price s{color:var(--muted);margin-right:10px}
.product .price b{font-size:13px}
.product .reviews{margin-top:14px;font-size:11px;color:#444;display:flex;gap:30px}
.stars{color:#ccc;letter-spacing:1px;font-size:14px;line-height:1}
.stars b{color:var(--orange);font-weight:400}
.product .btn{margin:14px 0 0 40px;width:116px;height:27px;font-size:10px}
.side-arrow{color:#999;font-size:46px;font-weight:300;line-height:1}

/* promo */
.promo{left:91px;top:1640px;width:1010px;height:189px}
.promo .wood{left:0;top:0;width:523px;height:189px;background:linear-gradient(90deg,#3a2215,#5a3520 50%,#46291a)}
.promo .photo{left:523px;top:0;width:487px;height:189px;background:linear-gradient(135deg,#6c6c68,#a3a29a 45%,#4a4a46)}
.promo-text{left:95px;top:42px;font-family:"Oswald",Arial,sans-serif;font-weight:600;font-size:45px;line-height:1.18;color:#fff}
.promo-text span{color:var(--orange)}
.promo-btn{left:578px;top:91px;width:118px;height:26px;font-size:10px}

/* shipping */
.shipping{left:91px;top:2381px;width:1010px;height:119px;border:2px dashed #bdbdbd}
.ship-text{left:110px;top:43px;font-size:25px;font-weight:700;color:#111;white-space:nowrap;letter-spacing:-.3px}
.ship-text span{color:var(--orange)}

/* instagram */
.insta{width:210px;height:198px;border:1px solid var(--line)}
.insta.hl{border:2px solid #c6d6ef}

/* footer */
.footer{left:0;top:2908px;width:1200px;height:220px;background:var(--footer)}
.fcol h5{color:#e6e6e6;font-size:14px;font-weight:600;letter-spacing:3px;margin-bottom:16px}
.fcol p{color:var(--footer-text);font-size:12px;line-height:27px}
.news{width:227px;height:38px;display:flex}
.news .in{flex:1;background:#2a2a2a;color:#999;font-size:11px;padding-left:10px;line-height:38px}
.news .go{width:38px;background:var(--blue);color:#fff;font-size:18px;text-align:center;line-height:36px}
.bottom{left:0;top:3128px;width:1200px;height:47px;background:#fff;font-size:10px;color:#444}
.pay{right:88px;top:14px;display:flex;gap:12px}
.pay i{width:40px;height:18px;background:#d8d8d8;border-radius:3px}
</style>
</head>
<body>

<div class="abs topbar">
  <div class="abs contact"><span><i class="ico-sq"></i>support@ridgemantis.com</span><span>| &nbsp; +61 400 555 019</span></div>
  <div class="abs util"><span><b>My Account</b> ▾</span><span>Currency: AUD ▾</span><span>Language: <i class="flag"></i>English ▾</span></div>
</div>

<header class="abs header">
  <div class="abs logo"><span class="logo-mark"></span><span class="logo-name">RIDGEMANTIS</span></div>
  <div class="abs search"><span class="cat">All Categories ▾</span><span class="field">Enter your search…</span>
    <svg width="14" height="14" viewBox="0 0 14 14"><circle cx="6" cy="6" r="4.5" fill="none" stroke="#222" stroke-width="2"/><path d="M9.5 9.5L13 13" stroke="#222" stroke-width="2"/></svg>
  </div>
  <div class="abs cart">0 item <em>in your cart</em></div>
  <svg class="abs cart-icon" width="36" height="32" viewBox="0 0 36 32"><path d="M6 12h20l-2 14H8z" fill="none" stroke="#fff" stroke-width="2.5"/><path d="M11 12a5 6 0 0 1 10 0" fill="none" stroke="#fff" stroke-width="2.5"/><circle cx="28" cy="24" r="6" fill="#fff"/></svg>
</header>

<nav class="abs nav">
  <a style="left:89px">HOME</a>
  <a class="active" style="left:159px">CATAGORIES<span class="caret">▼</span></a>
  <a style="left:296px">FOOTWEAR<span class="caret">▼</span></a>
  <a style="left:411px">OPTICS</a>
  <a style="left:502px">SHOOTING</a>
  <a style="left:612px">ACCESSORIES<span class="caret">▼</span></a>
  <a style="left:751px">BLINDS &amp; STANDS<span class="caret">▼</span></a>
  <a style="left:929px">HUNTING ACCESSORIES</a>
</nav>

<section class="abs hero" role="img" aria-label="Hunter in camouflage glassing with binoculars against an orange sunset"></section>
<div class="abs hero-title">OUTDOOR ACCESSORIES</div>
<div class="abs btn hero-btn">Shop Now</div>
<div class="abs arrow" style="left:104px;top:352px">‹</div>
<div class="abs arrow" style="left:1062px;top:352px">›</div>
<div class="abs dots"><i></i><i class="on"></i><i></i><i></i></div>

<div class="abs dropdown">
  <ul><h4>CAMPING</h4><li>VESTIBULUM</li><li>MAURISDUI</li><li>POSUEREQUIS</li><li>PULVINAR NO</li></ul>
  <ul><h4>DIRT BIKE</h4><li>VESTIBULUM</li><li>MAURISDUI</li><li>POSUEREQUIS</li><li>PULVINAR NO</li></ul>
</div>

<!-- category tiles -->
<div class="abs tile" style="left:91px;top:652px;background:linear-gradient(160deg,#5b6a78,#7c858a 45%,#3e3b30)" role="img" aria-label="Tent pitched on a mountain slope"><div class="frame"><span class="l1">Camping</span><span class="l2">Acessories</span></div></div>
<div class="abs tile" style="left:442px;top:652px;background:linear-gradient(160deg,#3c4034,#55584a 50%,#2a2c24)" role="img" aria-label="Dirt bike parked on a trail"><div class="frame"><span class="l1">Dirt Bike</span><span class="l2">Accessories</span></div></div>
<div class="abs tile" style="left:792px;top:652px;background:linear-gradient(180deg,#7d8e9a,#5f7784 45%,#49604f)" role="img" aria-label="Angler wading in a river"><div class="frame"><span class="l1">Fishing</span><span class="l2">Accessories</span></div></div>
<div class="abs tile" style="left:91px;top:904px;background:linear-gradient(180deg,#3e4f78,#c2652a 60%,#2a1a12)" role="img" aria-label="Hiker on a ridge at sunset"><div class="frame"><span class="l1">Tracking</span><span class="l2">Acessories</span></div></div>
<div class="abs tile" style="left:442px;top:904px;background:linear-gradient(160deg,#6a6a60,#4c4a40 55%,#33322b)" role="img" aria-label="Hunter in grassland"><div class="frame"><span class="l1">Hunting</span><span class="l2">Acessories</span></div></div>
<div class="abs tile" style="left:792px;top:904px;background:linear-gradient(180deg,#3f5c8a,#8e7a55 55%,#5a4a30)" role="img" aria-label="Hunter standing in open country"><div class="frame"><span class="l1">View All</span><span class="l2">Colection</span></div></div>

<!-- featured -->
<h2 class="abs section-title" style="top:1160px">FEATURED PRODUCTS</h2>
<div class="abs underline" style="top:1215px"></div>
<div class="abs side-arrow" style="left:96px;top:1355px">‹</div>
<div class="abs side-arrow" style="left:1058px;top:1355px">›</div>

<div class="abs product" style="left:144px;top:1259px">
  <div class="img" role="img" aria-label="Camouflage tactical holster" style="background:radial-gradient(circle at 50% 50%,#8a7a58 0 28%,#fff 30%)"></div>
  <div class="name">Tactical Backpack Hunting</div>
  <div class="price"><s>$552.00</s><b>$250.00</b></div>
  <div class="reviews">Reviews <span class="stars"><b>★★★</b>★★</span></div>
  <div class="btn">Add to cart</div>
</div>
<div class="abs product" style="left:368px;top:1259px">
  <div class="img" role="img" aria-label="Black tactical backpack" style="background:radial-gradient(circle at 50% 50%,#1e1e1e 0 34%,#fff 36%)"></div>
  <div class="name">Outdoors Traverse EPS</div>
  <div class="price"><s>$552.00</s><b>$250.00</b></div>
  <div class="reviews">Reviews <span class="stars"><b>★★★</b>★★</span></div>
  <div class="btn">Add to cart</div>
</div>
<div class="abs product" style="left:593px;top:1259px">
  <div class="img" role="img" aria-label="Blue and white offroad helmet" style="background:radial-gradient(circle at 50% 50%,#2c4aa0 0 30%,#fff 32%)"></div>
  <div class="name">Offroad Helmet Blue</div>
  <div class="price"><s>$552.00</s><b>$250.00</b></div>
  <div class="reviews">Reviews <span class="stars"><b>★</b>★★★★</span></div>
  <div class="btn">Add to cart</div>
</div>
<div class="abs product" style="left:823px;top:1259px">
  <div class="img" role="img" aria-label="Red motocross racing jersey" style="background:radial-gradient(circle at 50% 50%,#b52a2a 0 32%,#fff 34%)"></div>
  <div class="name">Racing Hardwear Automatic</div>
  <div class="price"><s>$552.00</s><b>$250.00</b></div>
  <div class="reviews">Reviews <span class="stars"><b>★</b>★★★★</span></div>
  <div class="btn">Add to cart</div>
</div>

<!-- promo -->
<div class="abs promo">
  <div class="abs wood" role="img" aria-label="Dark timber boards"></div>
  <div class="abs photo" role="img" aria-label="Shooter aiming a scoped rifle"></div>
  <div class="abs promo-text">UP TO 50% OFF ON<br><span>HUNT GEAR</span></div>
  <div class="abs btn promo-btn">Shop Now</div>
</div>

<!-- best seller -->
<h2 class="abs section-title" style="top:1880px">BEST SELLER</h2>
<div class="abs underline" style="top:1935px"></div>
<div class="abs side-arrow" style="left:96px;top:2075px">‹</div>
<div class="abs side-arrow" style="left:1058px;top:2075px">›</div>

<div class="abs product" style="left:144px;top:1977px">
  <div class="img" role="img" aria-label="Camouflage tactical holster" style="background:radial-gradient(circle at 50% 50%,#8a7a58 0 28%,#fff 30%)"></div>
  <div class="name">Tactical Backpack Hunting</div>
  <div class="price"><s>$552.00</s><b>$250.00</b></div>
  <div class="reviews">Reviews <span class="stars"><b>★★★</b>★★</span></div>
  <div class="btn">Add to cart</div>
</div>
<div class="abs product" style="left:368px;top:1977px">
  <div class="img" role="img" aria-label="Black tactical backpack" style="background:radial-gradient(circle at 50% 50%,#1e1e1e 0 34%,#fff 36%)"></div>
  <div class="name">Outdoors Traverse EPS</div>
  <div class="price"><s>$552.00</s><b>$250.00</b></div>
  <div class="reviews">Reviews <span class="stars"><b>★★★</b>★★</span></div>
  <div class="btn">Add to cart</div>
</div>
<div class="abs product" style="left:593px;top:1977px">
  <div class="img" role="img" aria-label="Pair of survival knives with sheath" style="background:radial-gradient(circle at 50% 50%,#6b6a60 0 30%,#fff 32%)"></div>
  <div class="name">Hunting Survival Knife</div>
  <div class="price"><s>$552.00</s><b>$250.00</b></div>
  <div class="reviews">Reviews <span class="stars"><b>★</b>★★★★</span></div>
  <div class="btn">Add to cart</div>
</div>
<div class="abs product" style="left:823px;top:1977px">
  <div class="img" role="img" aria-label="Brown leather hunting boot" style="background:radial-gradient(circle at 50% 50%,#7a3e22 0 30%,#fff 32%)"></div>
  <div class="name">Hunting Boot</div>
  <div class="price"><s>$552.00</s><b>$250.00</b></div>
  <div class="reviews">Reviews <span class="stars"><b>★</b>★★★★</span></div>
  <div class="btn">Add to cart</div>
</div>

<!-- shipping -->
<div class="abs shipping">
  <svg class="abs" style="left:24px;top:30px" width="72" height="58" viewBox="0 0 72 58"><path d="M2 24L70 2 50 56 34 36z" fill="var(--orange)"/><path d="M34 36L70 2 26 30z" fill="var(--orange-dark)"/><path d="M26 30l4 20 4-14" fill="#c96d05"/></svg>
  <div class="abs ship-text">FREE POSTAGE <span>AUSTRALIA AND NZ</span> , INTERNATIONAL SHIPMENT EXTRA</div>
</div>

<!-- instagram -->
<h2 class="abs section-title" style="top:2544px">INSTAGRAM</h2>
<div class="abs underline" style="top:2599px"></div>
<div class="abs side-arrow" style="left:88px;top:2720px">‹</div>
<div class="abs side-arrow" style="left:1076px;top:2720px">›</div>
<div class="abs insta" style="left:133px;top:2646px;background:linear-gradient(180deg,#7aa6d6,#dfe8ef 50%,#7a6a58)" role="img" aria-label="Hikers climbing a snowy mountain"></div>
<div class="abs insta hl" style="left:368px;top:2646px;background:radial-gradient(circle at 50% 50%,#1e1e1e 0 32%,#fff 34%)" role="img" aria-label="Black tactical backpack"></div>
<div class="abs insta" style="left:607px;top:2646px;background:linear-gradient(180deg,#3a7fd0,#9cc3ea 55%,#5c8a3a)" role="img" aria-label="Hiker jumping on a mountain meadow"></div>
<div class="abs insta hl" style="left:847px;top:2646px;background:radial-gradient(circle at 50% 50%,#2c4aa0 0 30%,#fff 32%)" role="img" aria-label="Blue offroad helmet"></div>

<!-- footer -->
<footer class="abs footer">
  <div class="abs fcol" style="left:112px;top:42px"><h5>CONTACT</h5><p>2150 Banksia Street, Australia, AU 6015<br>800-555-0142<br>name@ridgemantis.com</p></div>
  <div class="abs fcol" style="left:356px;top:42px"><h5>SUPPORT</h5><p>Terms and Conditions<br>Privacy Policy<br>Return Policy</p></div>
  <div class="abs fcol" style="left:601px;top:42px"><h5>ABOUT</h5><p>About<br>News<br>Contact</p></div>
  <div class="abs fcol" style="left:844px;top:42px"><h5>BE IN THE KNOW</h5><p style="line-height:17px;width:220px">Sign up for the latest news, offers and styles</p>
    <div class="news" style="margin-top:14px"><span class="in">Your email</span><span class="go">→</span></div>
  </div>
</footer>
<div class="abs bottom">
  <div class="abs" style="left:112px;top:17px">© 2017, Ridgemantis. Powered by Hearthcart</div>
  <div class="abs pay"><i></i><i></i><i></i><i></i><i></i><i></i></div>
</div>

</body>
</html>
```